Scientific project description

Here is a project description related to cellular mechanics, showing above the forces acting on cells in the tissues of our body. The forces on single cells are there to depict how forces are acting on cells (pressure squeezes the cell, shear flow is pushing the upward parts of the cell, tension pulls one part of the cell, strain is stretching the whole cell; the single cell images are to be found also on the last page). Intense red/purple are used to indicate that the forces are stressful (the colors to be used do not need to be exactly like these colors). The picture in the middle is a view of cells (same picture on next page if that needs to be modified). At the left, a description of what happens when everything is going well, i.e. the body stays healthy. At the right, if you dysfunction you get disease. Green nuances were used to indicate health, brownish, perhaps not so pleasant nuances were used to indicate disease. Below are the steps of the project.

On the whole, we're rather happy with the concept description as such, but it should look a little bit nicer. To many color nuances give a "noisy" impression, fonts could be nicer, layout more crisp, and the text on the steps should be more readable. We would also like to have two versions of the same picture, one with black background, one with white.

Target Market(s)

Scientists that are evaluating our project

Requirements
Must have
• Easy to grasp the idea, easy to read and understand the underlying idea.
Nice to have
• Would be good to have the Concept title ("Vorlint Concept and Envisioned Project Progression) on top of the figure as indicated in the second brief picture submitted.

```html
<!DOCTYPE html>
<html lang="en">
<head>
<meta charset="utf-8">
<title>Vorlint Concept and Envisioned Project Progression</title>
<link href="https://fonts.googleapis.com/css2?family=Arimo:wght@400;700&display=swap" rel="stylesheet">
<style>
  :root {
    --ink: #111111;
    --force-red: #8b1a2b;
    --force-maroon: #6e1530;
    --force-brown: #5a0f12;
    --force-purple: #4c1a52;
    --swatch-1: #b0101a;
    --swatch-2: #7a1530;
    --swatch-3: #5e0d10;
    --swatch-4: #6a1470;
    --health: #1fbf1f;
    --disease: #d99a00;
    --cell-dark: #0f2a12;
    --cell-mid: #2f7a22;
    --cell-light: #7ccf3a;
    --timeline: #555555;
    --backdrop: #fbf8fd;
  }
  html, body { margin: 0; padding: 0; overflow: hidden; }
  body { width: 1200px; height: 848px; background: #ffffff; font-family: "Arimo", Arial, sans-serif; color: var(--ink); }
  .canvas { position: relative; width: 1200px; height: 848px; overflow: hidden; background: #ffffff; }
  .tissue-backdrop { position: absolute; left: 0; top: 68px; width: 1200px; height: 780px;
    background: radial-gradient(ellipse at 30% 30%, #efe6f5 0%, rgba(246,240,250,0.6) 40%, #ffffff 80%),
                radial-gradient(ellipse at 80% 70%, #f1eaf7 0%, #ffffff 60%);
    opacity: 0.8; }
  .figure { position: absolute; left: 0; top: 0; }
  .title { position: absolute; left: 78px; top: 18px; margin: 0; font-size: 22px; font-weight: 700; letter-spacing: 0.1px; }
  .legend { position: absolute; left: 131px; top: 133px; }
  .legend-label { font-size: 18px; font-weight: 700; margin: 0 0 6px; }
  .swatches { display: flex; gap: 7px; }
  .swatch { width: 18px; height: 18px; }
  .force-label { position: absolute; font-size: 16px; }
  .force-pressure { left: 157px; top: 274px; color: var(--force-red); }
  .force-shear { left: 333px; top: 231px; color: var(--force-maroon); }
  .force-tension { left: 566px; top: 143px; color: var(--force-brown); }
  .force-strain { left: 701px; top: 309px; color: var(--force-purple); }
  .hub-label { position: absolute; left: 363px; top: 565px; font-size: 27px; color: #ffffff; }
  .state { position: absolute; }
  .state-title { margin: 0; font-size: 20px; font-weight: 700; }
  .state-text { margin: 2px 0 0; font-size: 15px; line-height: 22px; }
  .state-fitness { left: 118px; top: 542px; }
  .state-frailty { right: 366px; top: 538px; text-align: right; }
  .outcome { position: absolute; font-size: 29px; font-weight: 700; margin: 0; }
  .outcome-health { left: 119px; top: 637px; color: var(--health); }
  .outcome-disease { left: 716px; top: 637px; color: var(--disease); }
  .progression { position: absolute; left: 930px; top: 0; margin: 0; padding: 0; list-style: none; font-size: 25px; line-height: 33px; }
  .step { position: absolute; left: 0; white-space: nowrap; }
</style>
</head>
<body>
<div class="canvas">
  <div class="tissue-backdrop" role="img" aria-label="Faint micrograph of tissue in pale lilac"></div>

  <svg class="figure" width="1200" height="848" viewBox="0 0 1200 848" xmlns="http://www.w3.org/2000/svg">
    <defs>
      <radialGradient id="cellView" cx="50%" cy="50%" r="60%">
        <stop offset="0" stop-color="var(--cell-mid)"/>
        <stop offset="0.55" stop-color="#1f4d1a"/>
        <stop offset="1" stop-color="var(--cell-dark)"/>
      </radialGradient>
      <radialGradient id="hubView" cx="50%" cy="45%" r="60%">
        <stop offset="0" stop-color="#1c3d18"/>
        <stop offset="0.5" stop-color="#3f9a2a"/>
        <stop offset="1" stop-color="#1a3a15"/>
      </radialGradient>
      <marker id="head-red" viewBox="0 0 10 10" refX="8" refY="5" markerWidth="5" markerHeight="5" orient="auto"><path d="M0,0 L10,5 L0,10 Z" fill="var(--force-red)"/></marker>
      <marker id="head-maroon" viewBox="0 0 10 10" refX="8" refY="5" markerWidth="5" markerHeight="5" orient="auto"><path d="M0,0 L10,5 L0,10 Z" fill="var(--force-maroon)"/></marker>
      <marker id="head-brown" viewBox="0 0 10 10" refX="8" refY="5" markerWidth="5" markerHeight="5" orient="auto"><path d="M0,0 L10,5 L0,10 Z" fill="var(--force-brown)"/></marker>
      <marker id="head-purple" viewBox="0 0 10 10" refX="8" refY="5" markerWidth="5" markerHeight="5" orient="auto"><path d="M0,0 L10,5 L0,10 Z" fill="var(--force-purple)"/></marker>
      <marker id="head-ink" viewBox="0 0 10 10" refX="8" refY="5" markerWidth="7" markerHeight="7" orient="auto"><path d="M0,0 L10,5 L0,10" fill="none" stroke="var(--ink)" stroke-width="2"/></marker>
    </defs>

    <!-- linking bubbles -->
    <g class="bubbles" fill="#5d9c48" opacity="0.3">
      <circle cx="252" cy="412" r="21"/><circle cx="295" cy="467" r="39"/>
      <circle cx="398" cy="353" r="21"/><circle cx="415" cy="416" r="38"/>
      <circle cx="555" cy="342" r="21"/><circle cx="532" cy="410" r="38"/>
      <circle cx="680" cy="413" r="21"/><circle cx="638" cy="465" r="39"/>
    </g>

    <!-- stressed cell views -->
    <path role="img" aria-label="Micrograph of cells squeezed by pressure" fill="url(#cellView)"
      d="M113,340 C150,325 200,358 268,330 C275,350 250,372 195,368 C150,366 118,360 113,340 Z"/>
    <path role="img" aria-label="Micrograph of cells deformed by shear flow" fill="url(#cellView)"
      d="M320,312 C340,298 410,300 455,250 C470,232 485,230 484,250 C480,290 430,318 380,326 C345,331 316,325 320,312 Z"/>
    <path role="img" aria-label="Micrograph of cells pulled by tension" fill="url(#cellView)"
      d="M528,235 C560,250 600,195 660,230 C660,260 640,295 600,298 C555,300 528,275 528,235 Z"/>
    <ellipse role="img" aria-label="Micrograph of cells stretched by strain" fill="url(#cellView)" cx="723" cy="361" rx="79" ry="24"/>

    <!-- central tissue view -->
    <path role="img" aria-label="Micrograph of a cell layer with green cytoskeleton and red markers" fill="url(#hubView)"
      d="M345,520 C330,470 380,447 460,448 C540,450 600,470 608,540 C615,610 600,690 530,712 C460,730 380,718 350,660 C335,620 355,560 345,520 Z"/>
    <rect x="358" y="563" width="222" height="36" fill="#0d1f0c" opacity="0.55"/>

    <!-- pressure -->
    <g stroke="var(--force-red)" stroke-width="3" marker-end="url(#head-red)">
      <line x1="128" y1="292" x2="128" y2="332"/><line x1="161" y1="292" x2="161" y2="338"/>
      <line x1="193" y1="292" x2="193" y2="343"/><line x1="226" y1="292" x2="226" y2="338"/>
      <line x1="257" y1="292" x2="257" y2="328"/>
    </g>
    <!-- shear -->
    <g stroke="var(--force-maroon)" stroke-width="3" marker-end="url(#head-maroon)">
      <line x1="323" y1="283" x2="372" y2="280"/><line x1="360" y1="268" x2="408" y2="264"/>
      <line x1="398" y1="248" x2="443" y2="244"/><line x1="432" y1="232" x2="474" y2="228"/>
    </g>
    <!-- tension -->
    <g stroke="var(--force-brown)" stroke-width="3" marker-end="url(#head-brown)">
      <line x1="563" y1="232" x2="563" y2="188"/><line x1="598" y1="212" x2="598" y2="165"/>
      <line x1="632" y1="232" x2="632" y2="188"/>
    </g>
    <!-- strain -->
    <g stroke="var(--force-purple)" stroke-width="3" marker-end="url(#head-purple)">
      <line x1="640" y1="345" x2="598" y2="345"/><line x1="640" y1="369" x2="598" y2="369"/>
      <line x1="806" y1="345" x2="848" y2="345"/><line x1="806" y1="369" x2="848" y2="369"/>
    </g>

    <!-- fitness arrow and frailty inhibitor -->
    <line x1="316" y1="580" x2="278" y2="580" stroke="var(--ink)" stroke-width="2.5" marker-end="url(#head-ink)"/>
    <line x1="658" y1="580" x2="626" y2="580" stroke="var(--ink)" stroke-width="2.5"/>
    <line x1="626" y1="571" x2="626" y2="589" stroke="var(--ink)" stroke-width="3"/>

    <!-- progression timeline -->
    <line x1="905" y1="155" x2="905" y2="616" stroke="var(--timeline)" stroke-width="2"/>
    <g class="milestones" fill="#ffffff" stroke="var(--timeline)" stroke-width="1.5">
      <circle cx="905" cy="187" r="7"/><circle cx="905" cy="240" r="7"/><circle cx="905" cy="292" r="7"/>
      <circle cx="905" cy="342" r="7"/><circle cx="905" cy="393" r="7"/><circle cx="905" cy="444" r="7"/>
      <circle cx="905" cy="530" r="7"/>
    </g>
    <g fill="var(--timeline)">
      <circle cx="905" cy="187" r="3.5"/><circle cx="905" cy="240" r="3.5"/><circle cx="905" cy="292" r="3.5"/>
      <circle cx="905" cy="342" r="3.5"/><circle cx="905" cy="393" r="3.5"/><circle cx="905" cy="444" r="3.5"/>
      <circle cx="905" cy="530" r="3.5"/>
    </g>
  </svg>

  <h1 class="title">Vorlint Concept and Envisioned Project Progression</h1>

  <div class="legend">
    <p class="legend-label">Forces on Cells</p>
    <div class="swatches">
      <span class="swatch" style="background:var(--swatch-1)"></span>
      <span class="swatch" style="background:var(--swatch-2)"></span>
      <span class="swatch" style="background:var(--swatch-3)"></span>
      <span class="swatch" style="background:var(--swatch-4)"></span>
    </div>
  </div>

  <span class="force-label force-pressure">Pressure</span>
  <span class="force-label force-shear">Shear</span>
  <span class="force-label force-tension">Tension</span>
  <span class="force-label force-strain">Strain</span>

  <span class="hub-label">Mechanostasis</span>

  <div class="state state-fitness">
    <p class="state-title">Cell Fitness</p>
    <p class="state-text">Functional cellular<br>machineries</p>
  </div>
  <div class="state state-frailty">
    <p class="state-title">Cell Frailty</p>
    <p class="state-text">Dysfunctional cellular<br>machineries</p>
  </div>

  <p class="outcome outcome-health">Health</p>
  <p class="outcome outcome-disease">Disease</p>

  <ol class="progression">
    <li class="step" style="top:171px">Therapies</li>
    <li class="step" style="top:224px">Prevention</li>
    <li class="step" style="top:275px">Critical Targets</li>
    <li class="step" style="top:326px">Cellular Machineries</li>
    <li class="step" style="top:377px">Disease Models</li>
    <li class="step" style="top:428px">Cell, Tissue and<br>Organ Responses</li>
    <li class="step" style="top:514px">Mechanical Force<br>Models</li>
  </ol>
</div>
</body>
</html>
```